MYLAR BAG FOR BLOOMA

Ive included a template for the design provided by the printer.

FRONT :
I'd like to match the box , i have a screenshot. I used an app to create it and the box printer somehow applied it. The app tells me the fonts, let me know if you would like the font names.

BACK SIDE :

DIRECTIONS FOR USE : THC TOLERANCE MAY VARY FROM PERSON TO PERSON. THE ACCEPTED RECOMMENDATION FOR A NEW USER IS 10 MG THC. REFERENCE THE AFFIXED TRALVO TAG FOR ACCURATE DOSAGE INFORMATION .

INGREDIENTS : RICE, SUGAR, THC EXTRACT, COCONUT OIL, ARTIFICIAL FLAVOR & COLOR, SALT, MALT SYRUP

ALLERGEN WARNING : CONTAINS COCONUT.
MADE IN A FACULTY THAT HANDLES PEANUTS AND OTHER TREE NUTS.

THE ACTUAL VALUE OF REPORTED CANNABINOIDS MAY VARY FROM THE REPORTED VALUE BY +/-10 %

ACTIVATION TIME :10-60 MIN

WARNING : FOR USE BY INDIVIDUALS 21 YRS OF AGE OR OLDER OR BY REGISTERED QUALIFYING PATIENTS ONLY. IT IS ILLEGAL TO DRIVE A MOTOR VEHICLE WHILE UNDER THE INFLUENCE OF MARIJUANA.

KEEP OUT OF REACH OF CHILDREN.

HARBORVALE SAFETY LINE CENTER
1 800 555 0147

WARNING : USE BY PREGNANT OR BREASTFEEDING WOMEN OR BY WOMEN WHO PLAN TO BECOME
PREGNANT MAY RESULT IN FETAL INJURY, PRETERM BIRTH, LOW BIRTHWEIGHT, OR DEVELOPMENTAL
PROBLEMS FOR THE CHILD.

MADE IN A MARIJUANA FACILITY

MADE & DISTRIBUTED BY MARLOWE'S TWIG COMPANY
LICENSE # BQ K 004736
(LOGO)
www.FENWILLOWS.INFO

• CMKY colors

```html
<!DOCTYPE html>
<html lang="en">
<head>
<meta charset="utf-8">
<title>Blooma Mylar Bag – Front, Back and Dieline</title>
<link rel="stylesheet" href="https://fonts.googleapis.com/css2?family=Titan+One&family=Montserrat:wght@400;500;600;700&display=swap">
<style>
:root{
  --bag-pink:#e8b0cd;
  --seal-pink:#e3a8c6;
  --cream-yellow:#f3eeab;
  --white:#ffffff;
  --badge-green:#1f6b3a;
  --dieline-green:#2a9a4a;
  --ink:#2b2b2b;
  --page:#ffffff;
  --display:'Titan One', sans-serif;
  --body:'Montserrat', sans-serif;
}
*{margin:0;padding:0;box-sizing:border-box}
html,body{width:1200px;height:862px;overflow:hidden;background:var(--page)}
.canvas{position:relative;width:1200px;height:862px}

/* bag panels */
.bag-panel{position:absolute;top:140px;width:378px;height:600px;background:var(--bag-pink);overflow:hidden}
.bag-panel.front{left:53px}
.bag-panel.back{left:465px}
.seal-band{position:absolute;left:0;right:0;top:0;height:44px;background:var(--seal-pink)}
.zip-track{position:absolute;left:26px;right:26px;top:60px;height:8px;border-top:1.5px solid rgba(255,255,255,.45);border-bottom:1.5px solid rgba(0,0,0,.06)}
.line{position:absolute;left:0;right:0;text-align:center;white-space:nowrap}
.display{font-family:var(--display);line-height:1;letter-spacing:.5px}
.spaced{font-family:var(--body);font-weight:500;letter-spacing:3px;color:var(--white)}
.white{color:var(--white)}
.yellow{color:var(--cream-yellow)}
.badge{position:absolute}
.wordmark{font-family:var(--display);color:var(--cream-yellow);line-height:.92;white-space:nowrap}
.wordmark.placed{position:absolute}

/* back layout */
.back-content{position:absolute;left:52px;top:126px;width:290px;display:flex;flex-direction:column}
.back-content .wordmark{font-size:36px;margin-bottom:14px}
.copy-block{font-family:var(--body);font-weight:500;color:var(--white);font-size:7.8px;letter-spacing:1.2px;line-height:10px}
.copy-block p{margin-bottom:8px}
.copy-block p:last-child{margin-bottom:0}
.warning-box{width:276px;border:2px dotted var(--white);padding:4px;margin-top:10px}
.warning-inner{background:var(--white);padding:4px 5px;font-family:var(--body);font-size:6.2px;line-height:8px;color:var(--ink)}
.warning-inner b{font-weight:700}
.safety-line{text-align:center;margin:2px 0}
.pregnancy-note{border:1.5px solid var(--bag-pink);padding:2px 4px;margin-top:3px}
.facility{width:276px;margin-top:9px;text-align:center;font-family:var(--body);font-weight:600;font-size:7px;letter-spacing:.8px;color:var(--white)}
.signoff{display:flex;align-items:center;gap:12px;margin:9px 0 0 38px}
.signoff .wordmark{font-size:15px;margin:0}
.distributor{font-family:var(--body);font-weight:500;font-size:7.6px;line-height:9.6px;letter-spacing:.4px;color:var(--white);white-space:nowrap}

/* dieline template */
.dieline{position:absolute;left:0;top:0}
.dim-label{position:absolute;font-family:Georgia, serif;font-size:12px;color:var(--ink)}
.dim-small{position:absolute;font-family:Georgia, serif;font-size:6px;color:var(--ink);transform:rotate(-90deg);transform-origin:left top}
.tpl-front{position:absolute;left:923px;top:88px;width:198px;height:295px}
.tpl-gusset{position:absolute;left:923px;top:396px;width:198px;height:84px}
.tpl-gusset .wordmark{position:absolute;left:12px;top:26px;font-size:13px}
.tpl-back{position:absolute;left:923px;top:500px;width:198px;height:282px;transform:rotate(180deg);padding:8px 10px 8px 14px;display:flex;flex-direction:column;gap:5px}
.tpl-back > .wordmark{font-size:22px}
.tpl-copy{font-family:var(--body);font-weight:500;color:var(--white);font-size:4.4px;letter-spacing:.7px;line-height:5.4px}
.tpl-copy p{margin-bottom:3px}
.tpl-warning{border:1px dotted var(--white);padding:2px}
.tpl-warning div{background:var(--white);padding:2px 3px;font-family:var(--body);font-size:3.4px;line-height:4.4px;color:var(--ink)}
.tpl-facility{text-align:center;font-family:var(--body);font-weight:600;font-size:3.8px;color:var(--white)}
.tpl-signoff{display:flex;align-items:center;gap:8px;margin-left:20px}
.tpl-signoff .wordmark{font-size:11px}
.tpl-signoff .distributor{font-size:3.8px;line-height:4.8px}
</style>
</head>
<body>
<main class="canvas">

  <!-- FRONT PANEL -->
  <section class="bag-panel front" aria-label="Bag front">
    <div class="seal-band"></div>
    <div class="zip-track"></div>
    <div class="line display white" style="top:118px;left:-40px;font-size:20px">ADULT - USE</div>
    <svg class="badge" style="left:280px;top:118px" width="64" height="62" viewBox="0 0 64 62" aria-hidden="true">
      <path d="M3 3 H61 L32 59 Z" fill="var(--badge-green)" stroke="var(--white)" stroke-width="2"/>
      <path d="M12 14 H52 L32 50 Z" fill="var(--white)"/>
    </svg>
    <div class="line display white" style="top:145px;left:-10px;font-size:52px">THC</div>
    <div class="line display yellow" style="top:208px;left:-10px;font-size:56px">CEREAL</div>
    <div class="line display white" style="top:300px;font-size:55px">FROSTED</div>
    <div class="line display white" style="top:356px;font-size:36px">STRAWBERRY</div>
    <div class="line display white" style="top:390px;font-size:40px">BLOOMA</div>
    <div class="line spaced" style="top:437px;font-size:12px">FROSTED STRAWBERRY</div>
    <div class="line spaced" style="top:452px;font-size:12px">CEREAL ENHANCED WITH THC</div>
    <div class="line display yellow" style="top:480px;font-size:34px">FEN</div>
    <div class="line display yellow" style="top:514px;font-size:34px">WILLOWS</div>
    <div class="line spaced" style="top:556px;font-size:12px">KEEP OUT OF REACH OF CHILDREN</div>
  </section>

  <!-- BACK PANEL -->
  <section class="bag-panel back" aria-label="Bag back">
    <div class="seal-band"></div>
    <div class="zip-track"></div>
    <div class="back-content">
      <div class="wordmark">FEN<br>WILLOWS</div>
      <div class="copy-block">
        <p>DIRECTIONS FOR USE : THC TOLERANCE MAY VARY FROM PERSON TO PERSON. THE ACCEPTED RECOMMENDATION FOR A NEW USER IS 10 MG THC. REFERENCE THE AFFIXED TRALVO TAG FOR ACCURATE DOSAGE INFORMATION.</p>
        <p>INGREDIENTS : RICE, SUGAR, THC EXTRACT, COCONUT OIL, ARTIFICIAL FLAVOR &amp; COLOR, SALT, MALT SYRUP</p>
        <p>ALLERGEN WARNING : CONTAINS COCONUT. MADE IN A FACULTY THAT HANDLES PEANUTS AND OTHER TREE NUTS.</p>
        <p>THE ACTUAL VALUE OF REPORTED CANNABINOIDS MAY VARY FROM THE REPORTED VALUE BY +/-10 %</p>
        <p>ACTIVATION TIME : 10-60 MIN</p>
      </div>
      <div class="warning-box">
        <div class="warning-inner">
          <p><b>WARNING :</b> FOR USE BY INDIVIDUALS 21 YRS OF AGE OR OLDER OR BY REGISTERED QUALIFYING PATIENTS ONLY. IT IS ILLEGAL TO DRIVE A MOTOR VEHICLE WHILE UNDER THE INFLUENCE OF MARIJUANA. KEEP OUT OF REACH OF CHILDREN.</p>
          <p class="safety-line">HARBORVALE SAFETY LINE CENTER<br>1 800 555 0147</p>
          <p class="pregnancy-note"><b>WARNING :</b> USE BY PREGNANT OR BREASTFEEDING WOMEN OR BY WOMEN WHO PLAN TO BECOME PREGNANT MAY RESULT IN FETAL INJURY, PRETERM BIRTH, LOW BIRTHWEIGHT, OR DEVELOPMENTAL PROBLEMS FOR THE CHILD.</p>
        </div>
      </div>
      <div class="facility">MADE IN A MARIJUANA FACILITY</div>
      <div class="signoff">
        <div class="wordmark">FEN<br>WILLOWS</div>
        <div class="distributor">MADE &amp; DISTRIBUTED BY<br>MARLOWE'S TWIG COMPANY<br>LICENSE # BQ K 004736<br>www.FENWILLOWS.INFO</div>
      </div>
    </div>
  </section>

  <!-- DIELINE TEMPLATE -->
  <svg class="dieline" width="1200" height="862" viewBox="0 0 1200 862" aria-label="Printer dieline">
    <rect x="910" y="28" width="224" height="820" fill="var(--bag-pink)" stroke="var(--dieline-green)" stroke-width="1"/>
    <g stroke="var(--dieline-green)" stroke-width=".8" fill="none">
      <line x1="910" y1="72" x2="1134" y2="72"/><line x1="910" y1="76" x2="1134" y2="76"/>
      <line x1="910" y1="383" x2="1134" y2="383"/><line x1="910" y1="493" x2="1134" y2="493"/>
      <line x1="910" y1="800" x2="1134" y2="800"/><line x1="910" y1="804" x2="1134" y2="804"/>
      <path d="M886 28 V88 M882 28 H890 M882 88 H890"/>
      <path d="M905 28 V46 M901 28 H909 M901 46 H909"/>
      <path d="M905 60 V88 M901 60 H909 M901 88 H909"/>
    </g>
    <g stroke="var(--dieline-green)" stroke-width=".8" fill="none" stroke-dasharray="5 4">
      <line x1="923" y1="28" x2="923" y2="848"/><line x1="1121" y1="28" x2="1121" y2="848"/>
      <line x1="910" y1="60" x2="1134" y2="60"/><line x1="910" y1="88" x2="1134" y2="88"/>
      <line x1="923" y1="370" x2="1121" y2="370"/>
      <rect x="923" y="396" width="198" height="84"/>
      <line x1="923" y1="506" x2="1121" y2="506"/>
      <line x1="910" y1="787" x2="1134" y2="787"/><line x1="910" y1="815" x2="1134" y2="815"/>
    </g>
  </svg>
  <div class="dim-label" style="left:988px;top:2px">130mm</div>
  <div class="dim-label" style="left:1140px;top:193px">206mm</div>
  <div class="dim-label" style="left:1140px;top:425px">64mm</div>
  <div class="dim-label" style="left:1140px;top:620px">206mm</div>
  <div class="dim-label" style="left:1003px;top:370px;font-size:9px">7.5mm</div>
  <div class="dim-small" style="left:874px;top:70px">35mm</div>
  <div class="dim-small" style="left:894px;top:44px">10mm</div>
  <div class="dim-small" style="left:894px;top:82px">16mm</div>

  <div class="tpl-front" aria-label="Dieline front panel">
    <div class="line display white" style="top:6px;left:-30px;font-size:11px">ADULT - USE</div>
    <svg class="badge" style="left:152px;top:7px" width="38" height="34" viewBox="0 0 64 58" aria-hidden="true">
      <path d="M3 3 H61 L32 55 Z" fill="var(--badge-green)" stroke="var(--white)" stroke-width="2"/>
      <path d="M12 13 H52 L32 47 Z" fill="var(--white)"/>
    </svg>
    <div class="line display white" style="top:22px;left:-6px;font-size:29px">THC</div>
    <div class="line display yellow" style="top:56px;font-size:31px">CEREAL</div>
    <div class="line display white" style="top:110px;font-size:31px">FROSTED</div>
    <div class="line display white" style="top:142px;font-size:21px">STRAWBERRY</div>
    <div class="line display white" style="top:163px;font-size:22px">BLOOMA</div>
    <div class="line spaced" style="top:190px;font-size:7.5px;letter-spacing:1.6px">FROSTED STRAWBERRY</div>
    <div class="line spaced" style="top:199px;font-size:7.5px;letter-spacing:1.6px">CEREAL ENHANCED WITH THC</div>
    <div class="line display yellow" style="top:214px;font-size:20px">FEN</div>
    <div class="line display yellow" style="top:234px;font-size:20px">WILLOWS</div>
    <div class="line spaced" style="top:266px;font-size:7.5px;letter-spacing:1.6px">KEEP OUT OF REACH OF CHILDREN</div>
  </div>

  <div class="tpl-gusset" aria-label="Dieline gusset">
    <div class="wordmark">FEN<br>WILLOWS</div>
    <div class="line display white" style="left:70px;top:14px;font-size:19px">FROSTED</div>
    <div class="line display white" style="left:70px;top:34px;font-size:14px">STRAWBERRY</div>
    <div class="line display white" style="left:70px;top:48px;font-size:14px">BLOOMA</div>
  </div>

  <div class="tpl-back" aria-label="Dieline back panel">
    <div class="wordmark">FEN<br>WILLOWS</div>
    <div class="tpl-copy">
      <p>DIRECTIONS FOR USE : THC TOLERANCE MAY VARY FROM PERSON TO PERSON. THE ACCEPTED RECOMMENDATION FOR A NEW USER IS 10 MG THC. REFERENCE THE AFFIXED TRALVO TAG FOR ACCURATE DOSAGE INFORMATION.</p>
      <p>INGREDIENTS : RICE, SUGAR, THC EXTRACT, COCONUT OIL, ARTIFICIAL FLAVOR &amp; COLOR, SALT, MALT SYRUP</p>
      <p>ALLERGEN WARNING : CONTAINS COCONUT. MADE IN A FACULTY THAT HANDLES PEANUTS AND OTHER TREE NUTS.</p>
      <p>THE ACTUAL VALUE OF REPORTED CANNABINOIDS MAY VARY FROM THE REPORTED VALUE BY +/-10 %</p>
      <p>ACTIVATION TIME : 10-60 MIN</p>
    </div>
    <div class="tpl-warning"><div>
      <b>WARNING :</b> FOR USE BY INDIVIDUALS 21 YRS OF AGE OR OLDER OR BY REGISTERED QUALIFYING PATIENTS ONLY. IT IS ILLEGAL TO DRIVE A MOTOR VEHICLE WHILE UNDER THE INFLUENCE OF MARIJUANA. KEEP OUT OF REACH OF CHILDREN.<br>
      <span style="display:block;text-align:center">HARBORVALE SAFETY LINE CENTER<br>1 800 555 0147</span>
      <b>WARNING :</b> USE BY PREGNANT OR BREASTFEEDING WOMEN OR BY WOMEN WHO PLAN TO BECOME PREGNANT MAY RESULT IN FETAL INJURY, PRETERM BIRTH, LOW BIRTHWEIGHT, OR DEVELOPMENTAL PROBLEMS FOR THE CHILD.
    </div></div>
    <div class="tpl-facility">MADE IN A MARIJUANA FACILITY</div>
    <div class="tpl-signoff">
      <div class="wordmark">FEN<br>WILLOWS</div>
      <div class="distributor">MADE &amp; DISTRIBUTED BY<br>MARLOWE'S TWIG COMPANY<br>LICENSE # BQ K 004736<br>www.FENWILLOWS.INFO</div>
    </div>
  </div>

</main>
</body>
</html>
```